Business Card Design Project

I want a cleaner business card and envelope then what we have now, its too crowded.
Updates

I update with logo, this can be changed anyway you feel it looks best. I also have put gaurantee on there and extended time, this is my first time doing this. Also gave an example of current card

Target Market(s)

a wide array of customers from lattice 700 to small companies and cleints

Industry/Entity Type

Business

Requirements
Must have
• Need to have address, telephone number email
Nice to have
• a sharp professional card that stands out but is still very clean.
Should not have
• Not crazy looking

```html
<!DOCTYPE html>
<html lang="en">
<head>
<meta charset="utf-8">
<title>Design Presentation – Business Card Options</title>
<link href="https://fonts.googleapis.com/css2?family=Didact+Gothic&family=Questrial&display=swap" rel="stylesheet">
<style>
  :root {
    --paper: #ffffff;
    --ink: #1a1a1a;
    --text-grey: #444444;
    --card-border: #c9c9c9;
    --accent-red: #8c1c2c;
    --mark-grey: #8e8e8e;
    --band-grey: #d2d2d2;
    --fade-grey: #a8a8a8;
  }
  * { margin: 0; padding: 0; box-sizing: border-box; }
  html, body { width: 1200px; height: 849px; overflow: hidden; background: var(--paper); }
  body { position: relative; font-family: "Didact Gothic", "Century Gothic", sans-serif; color: var(--ink); }

  .sheet-title {
    position: absolute; left: 22px; top: 50px;
    font-family: "Questrial", "Century Gothic", sans-serif;
    font-weight: 400; font-size: 40px; letter-spacing: -1.5px; line-height: 1;
  }

  .card {
    position: absolute; width: 364px; height: 201px;
    border: 1px solid var(--card-border); background: var(--paper); overflow: hidden;
  }
  .card--front-1 { left: 228px; top: 184px; }
  .card--back-1  { left: 608px; top: 184px; }
  .card--front-2 { left: 228px; top: 444px; }
  .card--back-2  { left: 608px; top: 444px; }

  .option-label {
    position: absolute; left: 229px; font-size: 15px; color: var(--ink);
  }
  .option-label--1 { top: 387px; }
  .option-label--2 { top: 647px; }

  /* Front: brand block */
  .brand {
    position: absolute; left: 0; right: 0; top: 57px; text-align: center;
  }
  .brand__square {
    display: block; width: 52px; height: 52px; margin: 0 auto 7px;
    background: var(--mark-grey);
  }
  .brand__name {
    font-size: 14px; letter-spacing: 2.6px; line-height: 1.15;
    text-transform: uppercase; color: var(--ink);
  }
  .brand__web {
    margin-top: 5px; font-size: 9.5px; letter-spacing: 1.1px; color: var(--text-grey);
  }

  /* Back: contact layout */
  .card--back { background: linear-gradient(to right, var(--fade-grey) 0%, #e6e6e6 18%, var(--paper) 45%); }
  .contact__name {
    position: absolute; left: 15px; top: 44px; font-size: 13px; color: var(--accent-red);
  }
  .contact__role {
    position: absolute; left: 15px; top: 63px; font-size: 9px; color: var(--text-grey);
  }
  .contact__lines {
    position: absolute; left: 15px; top: 125px; list-style: none;
    font-size: 9px; line-height: 12.6px; color: var(--text-grey);
  }
  .contact__address {
    position: absolute; left: 238px; top: 151px; font-style: normal;
    font-size: 9px; line-height: 12.6px; color: var(--text-grey);
  }

  .side-band {
    position: absolute; right: 0; top: 0; width: 26px; height: 100%;
    background: var(--band-grey);
  }

  .corner-brand {
    position: absolute; left: 255px; top: 57px; width: 80px; text-align: center;
  }
  .corner-brand__square {
    display: block; width: 54px; height: 54px; margin: 0 auto 4px; background: var(--mark-grey);
  }
  .corner-brand__name { font-size: 7px; letter-spacing: 0.8px; text-transform: uppercase; color: var(--text-grey); }
</style>
</head>
<body>

<h1 class="sheet-title">DesignPresentation</h1>

<!-- Option 1 -->
<div class="card card--front-1">
  <div class="brand">
    <span class="brand__square"></span>
    <p class="brand__name">Harbor Crest<br>Insurance Group</p>
    <p class="brand__web">www.harborcrestagency.com</p>
  </div>
</div>

<div class="card card--back card--back-1">
  <span class="side-band"></span>
  <p class="contact__name">Marla Quinn-Toby</p>
  <p class="contact__role">Operation Manager</p>
  <ul class="contact__lines">
    <li>Tel: 555-210-4400 Ext. 214</li>
    <li>Dir: 555-210-4417</li>
    <li>Fax: 555-210-4403</li>
    <li>mquinn-toby@harborcrestagency.com</li>
  </ul>
  <address class="contact__address">18200 Alder Creek Ave.<br>Maple Ridge, MI 48000</address>
</div>

<p class="option-label option-label--1">option 1</p>

<!-- Option 2 -->
<div class="card card--front-2">
  <div class="brand">
    <span class="brand__square"></span>
    <p class="brand__name">Harbor Crest<br>Insurance Group</p>
    <p class="brand__web">www.harborcrestagency.com</p>
  </div>
</div>

<div class="card card--back card--back-2">
  <div class="corner-brand">
    <span class="corner-brand__square"></span>
    <p class="corner-brand__name">Harbor Crest</p>
  </div>
  <p class="contact__name">Marla Quinn-Toby</p>
  <p class="contact__role">Operation Manager</p>
  <ul class="contact__lines">
    <li>Tel: 555-210-4400 Ext. 214</li>
    <li>Dir: 555-210-4417</li>
    <li>Fax: 555-210-4403</li>
    <li>mquinn-toby@harborcrestagency.com</li>
  </ul>
  <address class="contact__address">18200 Alder Creek Ave.<br>Maple Ridge, MI 48000</address>
</div>

<p class="option-label option-label--2">option 2</p>

</body>
</html>
```